wooden jewelry - pearl necklaces

I sell wooden jeweler (rings and pearls) on markets, and so on. I also opened my business as a carpenter. The rings and a combination of wood and metal. The wood is special wood, not very common on Europe. I paint the rings afterwards. You can see some of the pictures on the pictures I uploaded. The pearls are made of the same kind of wood and colored in all kinds of colors. They are then assembled to bracelets. The jewelry is very individual and looks really cool and all kinds of people.

Target Market(s)

Young urban alternative with a sense of individuality

Contact Information for Business Card

Front:

Text:

„Kugelwerk“ (big)
„Malte Oswitz“ (smaler)

Back
„Holzschmuck
Herstellung von individuellem Holz- und Modeschmuck

Malte Oswitz
Tel: 015239460518
Lindgarbweg 9
83127 Burghausen

malteoswitz@postfeld.de“

Font styles to use
Sans Serif

Requirements
Nice to have
• Nice to see a camel thorn tree on the background, this is a special wood and some of the rings are made out of this wood.

```html
<!DOCTYPE html>
<html lang="de">
<head>
<meta charset="utf-8">
<title>Kugelwerk – Visitenkarte</title>
<link href="https://fonts.googleapis.com/css2?family=Roboto:wght@300;400;500;700&display=swap" rel="stylesheet">
<style>
  :root {
    --page: #5c5c5c;
    --card: #000000;
    --cream: #f5e29a;
    --coral: #ee4247;
    --ink-soft: #f1e3b3;
    --beads-a: #2b2320;
    --beads-b: #141110;
  }
  * { margin: 0; padding: 0; box-sizing: border-box; }
  html, body { width: 1200px; height: 1200px; overflow: hidden; }
  body {
    background: var(--page);
    font-family: "Roboto", Arial, sans-serif;
    position: relative;
  }
  .card {
    position: absolute;
    left: 200px;
    width: 820px;
    height: 470px;
    border-radius: 32px;
    overflow: hidden;
    background: var(--card);
  }
  .card--front { top: 46px; }
  .card--back { top: 624px; height: 468px; }

  .bead-photo {
    position: absolute; inset: 0;
    background: radial-gradient(ellipse at 40% 35%, var(--beads-a), var(--beads-b) 75%);
  }

  .brand-mark {
    position: absolute;
    border-radius: 50%;
    background: var(--cream);
  }
  .brand-name {
    position: absolute;
    color: var(--cream);
    font-weight: 700;
    text-align: center;
    letter-spacing: 0.5px;
    white-space: nowrap;
    transform: translateX(-50%);
  }

  .card--front .brand-mark { left: 176px; top: 164px; width: 80px; height: 80px; }
  .card--front .brand-name { left: 216px; top: 280px; font-size: 29px; }

  .divider {
    position: absolute;
    left: 410px; top: 156px;
    width: 2px; height: 156px;
    background: var(--cream);
  }

  .person {
    position: absolute;
    left: 610px; top: 196px;
    transform: translateX(-50%);
    text-align: center;
    white-space: nowrap;
  }
  .person__name {
    font-size: 38px;
    font-weight: 500;
    color: var(--cream);
    line-height: 1.1;
  }
  .person__role {
    font-size: 19px;
    font-weight: 300;
    color: var(--cream);
  }

  .contact {
    position: absolute;
    top: 382px;
    display: flex;
    align-items: center;
    gap: 8px;
    color: var(--ink-soft);
    font-size: 19px;
    font-weight: 300;
    line-height: 24px;
    white-space: nowrap;
  }
  .contact__icon { width: 26px; height: 26px; flex: none; }
  .contact--address { left: 45px; }
  .contact--phone { left: 301px; }
  .contact--web { left: 523px; }

  .band { position: absolute; left: 0; width: 100%; }
  .card--front .band { top: 437px; height: 33px; }
  .card--back .band { top: 438px; height: 30px; }

  .card--back .brand-mark { left: 363px; top: 160px; width: 96px; height: 96px; }
  .card--back .brand-name { left: 411px; top: 302px; font-size: 38px; }

  .website {
    position: absolute;
    left: 411px; top: 408px;
    transform: translateX(-50%);
    display: flex; align-items: center; gap: 8px;
    color: var(--ink-soft);
    font-size: 18px;
    font-weight: 300;
    white-space: nowrap;
  }
  .website svg { width: 18px; height: 18px; }
</style>
</head>
<body>

<section class="card card--front">
  <div class="bead-photo" role="img" aria-label="Dunkles Foto bunter Holzperlen als Kartenhintergrund"></div>

  <div class="brand-mark"></div>
  <div class="brand-name">KUGELWERK</div>

  <div class="divider"></div>

  <div class="person">
    <div class="person__name">Malte Oswitz</div>
    <div class="person__role">Holzschmuck</div>
  </div>

  <div class="contact contact--address">
    <svg class="contact__icon" viewBox="0 0 26 26">
      <circle cx="13" cy="13" r="13" fill="var(--coral)"/>
      <path d="M6 13.5 13 7l7 6.5h-2.2V19h-3.3v-4h-3v4H8.2v-5.5z" fill="#fff"/>
    </svg>
    <div>Lindgarbweg 9<br>83127 Burghausen</div>
  </div>

  <div class="contact contact--phone">
    <svg class="contact__icon" viewBox="0 0 26 26">
      <circle cx="13" cy="13" r="13" fill="var(--coral)"/>
      <circle cx="13" cy="13" r="7.5" fill="none" stroke="#fff" stroke-width="1.4"/>
      <path d="M10 9.5c.6-.4 1.2 0 1.5.7l.4 1c.1.4 0 .8-.4 1l-.4.3c.4 1 1.1 1.7 2 2.1l.3-.4c.3-.3.7-.4 1-.3l1 .5c.6.3.9.9.5 1.5-.6.9-1.6 1-2.5.6-1.9-.8-3.3-2.3-4-4.2-.3-.9-.1-2 .6-2.8z" fill="#fff"/>
    </svg>
    <div>015239460518<br>015239460518</div>
  </div>

  <div class="contact contact--web">
    <svg class="contact__icon" viewBox="0 0 26 26">
      <circle cx="13" cy="13" r="13" fill="var(--coral)"/>
      <circle cx="13" cy="13" r="7" fill="#fff"/>
      <path d="M9 10c1.5-.5 2.5.3 2.6 1.6.1 1-1 1.3-1 2.4 0 .8-.7 1.3-1.6 1.1zm5.5-3c.3 1.2 1.6 1.2 2.3 2 .7 1-.3 2 .5 3 .6.8 1.4.3 1.6-.5" fill="var(--coral)"/>
    </svg>
    <div>malteoswitz@postfeld.de<br>www.kugelwerk-schmuck.de</div>
  </div>

  <svg class="band" viewBox="0 0 820 33" preserveAspectRatio="none">
    <polygon points="0,0 410,0 402,33 0,33" fill="var(--coral)"/>
    <polygon points="421,0 820,0 820,33 413,33" fill="var(--cream)"/>
  </svg>
</section>

<section class="card card--back">
  <div class="brand-mark"></div>
  <div class="brand-name">KUGELWERK</div>

  <div class="website">
    <svg viewBox="0 0 18 18">
      <circle cx="9" cy="9" r="8" fill="var(--ink-soft)"/>
      <path d="M4.5 6c1.7-.5 2.8.3 2.9 1.8.1 1.1-1.1 1.4-1.1 2.6 0 .9-.8 1.4-1.8 1.2zm6-3.4c.3 1.3 1.8 1.3 2.6 2.2.8 1.1-.3 2.2.6 3.3.6.9 1.6.3 1.8-.6" fill="var(--card)"/>
    </svg>
    <span>www.kugelwerk-schmuck.de</span>
  </div>

  <svg class="band" viewBox="0 0 820 30" preserveAspectRatio="none">
    <polygon points="0,0 416,0 408,30 0,30" fill="var(--coral)"/>
    <polygon points="434,0 820,0 820,30 426,30" fill="var(--cream)"/>
  </svg>
</section>

</body>
</html>
```